Business Card Design Project

We consult with hotels on setting rates and maximizing a revenue strategy

Industry/Entity Type

Business

Contact Information for Business Card

I am not sure what I want. Our company offers high level consulting to hotels around the country but we are also laid back. I would like something that is professional but also shows the laid back side

```html
<!DOCTYPE html>
<html lang="en">
<head>
<meta charset="utf-8">
<title>Crestline Revenue Management Solutions – Business Card</title>
<link href="https://fonts.googleapis.com/css2?family=Exo+2:wght@700&family=PT+Sans:wght@400;700&display=swap" rel="stylesheet">
<style>
  :root {
    --stage: #4a3436;
    --teal: #5a9db0;
    --teal-deep: #4f93a8;
    --ink: #2e2520;
    --paper: #ffffff;
  }
  html, body {
    margin: 0;
    width: 1200px;
    height: 1200px;
    overflow: hidden;
    background: var(--stage);
  }
  .card {
    position: absolute;
    left: 194px;
    width: 811px;
    height: 460px;
    background: var(--paper);
    overflow: hidden;
    font-family: "PT Sans", sans-serif;
    color: var(--ink);
  }
  /* Front */
  .card--front { top: 106px; }
  .card--front .sky {
    position: absolute; inset: 0 0 auto 0; height: 350px;
    background: linear-gradient(to bottom, var(--teal) 0%, #8fbfcc 60%, #ffffff 100%);
  }
  .front-mark {
    position: absolute; left: 0; right: 0; top: 258px;
    display: flex; flex-direction: column; align-items: center;
  }
  .wordmark {
    font-family: "Exo 2", sans-serif;
    font-weight: 700;
    color: var(--ink);
    line-height: 1;
    margin: 0;
  }
  .front-mark .wordmark { font-size: 50px; letter-spacing: 1px; }
  .front-mark .tagline-band {
    margin-top: 6px;
    background: var(--ink);
    color: var(--paper);
    font-weight: 700;
    font-size: 18px;
    padding: 6px 12px;
  }
  .front-web {
    position: absolute; left: 0; right: 0; top: 402px;
    text-align: center; font-size: 20px;
  }
  /* Back */
  .card--back { top: 634px; }
  .card--back .sky {
    position: absolute; inset: 0;
    background: linear-gradient(160deg, var(--teal-deep) 0%, #9cc8d3 22%, #ffffff 42%);
  }
  .back-id {
    position: absolute; left: 318px; top: 62px;
  }
  .back-id .wordmark { font-size: 60px; letter-spacing: 2px; }
  .back-id .legal { font-size: 23px; margin-top: 6px; }
  .person { position: absolute; left: 318px; top: 204px; }
  .person .name { font-weight: 700; font-size: 30px; color: var(--teal); margin: 0; line-height: 1.1; }
  .person .role { font-size: 20px; margin-top: 4px; }
  .contact { position: absolute; left: 318px; top: 300px; font-size: 20px; line-height: 27px; }
  .contact .label { color: var(--teal); }
  .band { position: absolute; left: 0; bottom: 0; width: 811px; height: 60px; }
  .band-web {
    position: absolute; left: 318px; bottom: 14px;
    color: var(--paper); font-size: 25px; letter-spacing: 6.5px;
  }
</style>
</head>
<body>
  <section class="card card--front">
    <div class="sky"></div>
    <div class="front-mark">
      <p class="wordmark">CRESTLINE</p>
      <div class="tagline-band">Revenue Management Solutions</div>
    </div>
    <div class="front-web">www.CrestlineRMS.com</div>
  </section>

  <section class="card card--back">
    <div class="sky"></div>
    <div class="back-id">
      <p class="wordmark">CRESTLINE</p>
      <div class="legal">Revenue Management Solutions LLC</div>
    </div>
    <div class="person">
      <p class="name">Dana Whitfield</p>
      <div class="role">Regional Revenue Manager</div>
    </div>
    <div class="contact">
      <div><span class="label">Office</span> 555-310-4827</div>
      <div><span class="label">Fax</span> 555-310-4890</div>
      <div><span class="label">Email</span> Dana@CrestlineRMS.com</div>
    </div>
    <svg class="band" viewBox="0 0 811 60" aria-hidden="true">
      <path d="M210 60 C240 30 270 6 300 0 L811 0 L811 60 Z" fill="var(--ink)"/>
    </svg>
    <div class="band-web">www.CrestlineRMS.com</div>
  </section>
</body>
</html>
```